Love cats? Love the planet? We need a design for the most eco-friendly cat grass kit box ever!

We need a box designed for our new product - the world's most eco-friendly cat grass kit ever!

Text and documents attached. Text can be copied and pasted. It has been spell-checked already.

Some pictures need to be sourced and/or drawn.

It needs to be eye-catching in its simplicity and minimalism. Not too many colors, swirls, curlicues and stuff. Just simple. And the 'green' nature of it (biodegradability, 'save the planet', recycle, re-use, sustainable contents etc needs to be visible from a distance to stand out from the crowd).

Final design needs to communicate love of cats and the planet.

Target Market(s)

Apartment-dwelling cat owners

Industry/Entity Type

Pet Care

Font styles to use
Other font styles liked:
• Comfortaa

Colors

Designer to choose colors to be used in the design.

Requirements
Must have
• Clear, clean, simple and eye-catching design. Not overloaded with images and text. A cute cartoon/drawn cat munching on the cat grass.
• A drawn pot that heavily matches the actual pot in terms of color, shape and texture.

```html
<!DOCTYPE html>
<html lang="en">
<head>
<meta charset="utf-8">
<title>Leafpaw – Cat Grass Kit Box</title>
<link rel="stylesheet" href="https://fonts.googleapis.com/css2?family=Varela+Round&display=swap">
<style>
  :root {
    --sky-top: #5fa9d6;
    --sky-mid: #9fcfe8;
    --sky-low: #dff0f8;
    --scene-light: #e9f4ec;
    --grass: #6bb82e;
    --grass-dark: #3f8f1f;
    --brand-green: #7cbf2a;
    --cat-orange: #f2a12e;
    --bubble: #fbe7c8;
    --bubble-text: #e0841e;
    --label-orange: #ef8a1c;
    --panel-white: #ffffff;
    --ink: #4a4a4a;
    --page: #e4e4e4;
    --lid: #f1f1f4;
    --pot-tone: #8fb85a;
  }
  * { box-sizing: border-box; margin: 0; padding: 0; }
  html, body { width: 1200px; height: 896px; overflow: hidden; }
  body {
    background: var(--page);
    font-family: "Varela Round", sans-serif;
    position: relative;
  }
  .panel { position: absolute; overflow: hidden; }

  .brand { color: var(--brand-green); font-family: "Varela Round", sans-serif; font-weight: 400; line-height: 1; }
  .brand-dot { border-radius: 50%; background: var(--brand-green); flex: none; }

  /* Top lid */
  .lid {
    left: 170px; top: 16px; width: 300px; height: 300px;
    background: linear-gradient(180deg, var(--sky-top), var(--sky-mid));
  }
  .lid-badge {
    position: absolute; left: 30px; top: 70px; width: 240px; height: 160px;
    border-radius: 50%; background: var(--lid);
    display: flex; align-items: center; justify-content: center; gap: 10px;
  }
  .lid .brand { font-size: 40px; }
  .lid .brand-dot { width: 22px; height: 22px; }

  /* Front */
  .front {
    left: 40px; top: 316px; width: 560px; height: 560px;
    background: linear-gradient(180deg, var(--sky-top) 0%, var(--sky-mid) 45%, var(--sky-low) 100%);
  }
  .headline {
    position: absolute; right: 22px; top: 22px; width: 470px;
    color: #fff; font-size: 27px; line-height: 1.35; text-align: right;
  }
  .scene-art {
    position: absolute; left: 0; top: 330px; width: 560px; height: 230px;
    background: linear-gradient(180deg, var(--scene-light) 0%, var(--grass) 45%, var(--grass-dark) 100%);
  }
  .front-brand {
    position: absolute; left: 36px; top: 250px;
    display: flex; align-items: center; gap: 12px;
  }
  .front-brand .brand { font-size: 56px; }
  .front-brand .brand-dot { width: 32px; height: 32px; }
  .speech {
    position: absolute; left: 310px; top: 150px; width: 220px; height: 110px;
    border-radius: 50%; background: var(--bubble);
    display: flex; align-items: center; justify-content: center;
    padding: 0 26px;
  }
  .speech::after {
    content: ""; position: absolute; left: 70px; bottom: -16px;
    border-left: 10px solid transparent; border-right: 14px solid transparent;
    border-top: 22px solid var(--bubble);
  }
  .speech-text { color: var(--bubble-text); font-size: 13px; line-height: 1.3; text-align: center; }
  .cat-art {
    position: absolute; left: 340px; top: 290px; width: 190px; height: 250px;
    border-radius: 95px 95px 20px 20px;
    background: var(--cat-orange);
  }

  /* Side */
  .side { left: 600px; top: 316px; width: 560px; height: 560px; background: var(--panel-white); }
  .side-strip {
    position: absolute; left: 0; top: 0; width: 150px; height: 560px;
    background: linear-gradient(180deg, var(--sky-top), var(--sky-mid) 50%, var(--sky-low));
  }
  .mini-head {
    position: absolute; left: 10px; top: 40px; width: 130px;
    color: #fff; font-size: 15px; line-height: 1.35; text-align: center;
  }
  .mini-brand {
    position: absolute; left: 0; top: 170px; width: 150px;
    display: flex; justify-content: center; align-items: center; gap: 6px;
  }
  .mini-brand .brand { font-size: 26px; }
  .mini-brand .brand-dot { width: 14px; height: 14px; }
  .mini-scene {
    position: absolute; left: 0; top: 300px; width: 150px; height: 260px;
    background: linear-gradient(180deg, var(--sky-low) 0%, var(--grass) 55%, var(--grass-dark) 100%);
  }
  .mini-cat {
    position: absolute; left: 25px; top: 330px; width: 100px; height: 130px;
    border-radius: 50px 50px 12px 12px; background: var(--cat-orange);
  }

  .info { position: absolute; left: 150px; top: 0; width: 410px; height: 560px; padding: 24px 24px 20px; }
  .info-title { color: var(--brand-green); font-size: 21px; line-height: 1.3; font-weight: 400; }
  .pot-area { position: relative; height: 290px; margin-top: 14px; }
  .pot-photo {
    position: absolute; left: 120px; top: 0; width: 140px; height: 280px;
    border-radius: 8px;
    background: linear-gradient(180deg, var(--pot-tone), #9a8a5a);
  }
  .label { position: absolute; color: var(--label-orange); font-size: 11px; line-height: 1.3; width: 110px; }
  .label.left { left: 0; }
  .label.right { left: 272px; }
  .body-copy { margin-top: 22px; color: var(--ink); font-size: 11px; line-height: 1.45; width: 250px; }
  .recycle { position: absolute; left: 174px; bottom: 24px; width: 44px; height: 44px; border-radius: 50%; background: var(--grass); }
  .footer-copy { position: absolute; left: 230px; bottom: 30px; width: 220px; color: var(--ink); font-size: 10px; line-height: 1.4; }
</style>
</head>
<body>

  <section class="panel lid" aria-label="Box top">
    <div class="lid-badge">
      <span class="brand-dot"></span>
      <span class="brand">Leafpaw</span>
    </div>
  </section>

  <section class="panel front" aria-label="Box front">
    <div class="scene-art" role="img" aria-label="Illustrated white clouds and tall green cat grass across the bottom"></div>
    <p class="headline">The greenest cat grass kit... ever.<br>Seriously.</p>
    <div class="front-brand">
      <span class="brand-dot"></span>
      <span class="brand">Leafpaw</span>
    </div>
    <div class="speech">
      <p class="speech-text">Every purchase feeds 1 kitty cat stuck in a shelter, waiting on their forever-home.</p>
    </div>
    <div class="cat-art" role="img" aria-label="Cartoon orange tabby cat sitting in the grass"></div>
  </section>

  <section class="panel side" aria-label="Box side">
    <div class="side-strip">
      <p class="mini-head">The greenest cat grass kit... ever. Seriously.</p>
      <div class="mini-brand">
        <span class="brand-dot"></span>
        <span class="brand">Leafpaw</span>
      </div>
      <div class="mini-scene" role="img" aria-label="Illustrated cat grass"></div>
      <div class="mini-cat" role="img" aria-label="Small cartoon orange tabby cat"></div>
    </div>
    <div class="info">
      <h2 class="info-title">Everything you're holding can safely end up in your compost bin!</h2>
      <div class="pot-area">
        <p class="label left" style="top:10px">The pot: made from 100% plant fibre.</p>
        <p class="label left" style="top:70px">The seeds: organic wheatgrass, no sprays.</p>
        <p class="label left" style="top:130px">The soil: peat-free coir mix, home composted.</p>
        <p class="label left" style="top:200px">Bag: plant-based film that breaks down.</p>
        <div class="pot-photo" role="img" aria-label="Photo of cat grass growing in a fibre pot, cut away to show the soil"></div>
        <p class="label right" style="top:20px">Sow the seeds evenly</p>
        <p class="label right" style="top:110px">Keep soil damp</p>
        <p class="label right" style="top:200px">Plant it, water it, let it grow.</p>
      </div>
      <p class="body-copy">This box is printed with soy inks on recycled card. Flatten it and add it to your compost bin or paper recycling when done.</p>
    </div>
    <span class="recycle" aria-hidden="true"></span>
    <p class="footer-copy">Every part of this kit is plant-based and compostable.</p>
  </section>

</body>
</html>
```